Real Estate Renovation and Rental:Business Card/Logo Design Project

Dunleavy Group LLC is a small partnership that buys homes to renovate, then provide as rentals to people who may not currently be able to purchase a home - but we also coach them on how to improve their credit so that, in 2-5 years, they may be able to buy a home. Maybe even the one they're living in.

We are based in Sonoma County of Northern California, operating in communities including Healdsburg, Windsor, Santa Rosa, and Cloverdale.

Please design a business card, but the same logo should work for signs that we will post on the homes as they are being renovated.

The design should be clean, contemporary, professional but warm. I'd love to see a rooftop feature, or some other element of a house. Again, not too much detail, clean and welcoming. The design must include "Dunleavy Group LLC" - but "DGLLC" could also be used as a primary name, with "Dunleavy Group LLC" in smaller print somewhere. If using "DGLLC", the DG could be visually distinct (larger, different color, font) than the LLC part of the name but they must be together.
Updates

just conferring with partner to choose a final design ... should be ready to choose soon and will post

Industry/Entity Type

Business

Requirements
Must have
• the name "Dunleavy Group LLC"
for business card design, and leave room for us to customize with partner names, address, telephone numbers, email addresses
Nice to have
• some element of a house included

```html
<!DOCTYPE html>
<html lang="en">
<head>
<meta charset="utf-8">
<title>Dunleavy Group LLC – Business Card</title>
<link href="https://fonts.googleapis.com/css2?family=Archivo:wght@800&family=Arimo:wght@400&display=swap" rel="stylesheet">
<style>
  :root {
    --stage: #ececec;
    --card-white: #ffffff;
    --blue-top: #0a7ad6;
    --blue-mid: #003b86;
    --blue-deep: #241a63;
    --green-light: #7fbb30;
    --green-deep: #00912f;
    --brand-blue: #0b3e8f;
    --site-blue: #2a4f9a;
  }
  html, body {
    margin: 0;
    width: 1200px;
    height: 900px;
    overflow: hidden;
    background: var(--stage);
  }
  .canvas {
    position: relative;
    width: 1200px;
    height: 900px;
  }
  .card {
    position: absolute;
    left: 275px;
    width: 650px;
    height: 330px;
    border-radius: 20px;
    background: var(--card-white);
    overflow: hidden;
  }
  .card--front { top: 101px; }
  .card--back  { top: 468px; }

  .front-field {
    position: absolute;
    left: 0; top: 0;
    width: 612px;
    height: 100%;
    background: linear-gradient(180deg, var(--blue-top) 0%, var(--blue-mid) 62%, var(--blue-deep) 100%);
  }
  .front-band {
    position: absolute;
    left: 0; top: 0;
  }
  .brand {
    position: absolute;
    display: flex;
    align-items: center;
    gap: 8px;
    font-family: "Archivo", "Arial Black", sans-serif;
    font-weight: 800;
  }
  .brand__square { flex: none; }
  .brand__name { line-height: 1; }
  .brand__short { display: block; letter-spacing: -1px; }
  .brand__full  { display: block; margin-top: 3px; }

  .brand--front { left: 43px; top: 36px; color: var(--card-white); }
  .brand--front .brand__square { background: var(--card-white); width: 66px; height: 66px; }
  .brand--front .brand__short { font-size: 60px; }
  .brand--front .brand__full  { font-size: 18px; }

  .brand--back { left: 43px; top: 139px; color: var(--brand-blue); }
  .brand--back .brand__square { background: var(--brand-blue); width: 54px; height: 54px; }
  .brand--back .brand__short { font-size: 48px; }
  .brand--back .brand__full  { font-size: 14.5px; }

  .website {
    position: absolute;
    left: 612px;
    top: 0;
    width: 38px;
    height: 100%;
    display: flex;
    align-items: center;
    justify-content: center;
  }
  .website span {
    transform: rotate(-90deg);
    white-space: nowrap;
    font-family: "Arimo", Arial, sans-serif;
    font-size: 12px;
    letter-spacing: 1.5px;
    color: var(--site-blue);
  }
  .divider {
    position: absolute;
    left: 321px;
    top: 21px;
  }
</style>
</head>
<body>
<main class="canvas">
  <section class="card card--front" aria-label="Card front">
    <div class="front-field">
      <svg class="front-band" width="612" height="330" viewBox="0 0 612 330" aria-hidden="true">
        <defs>
          <linearGradient id="slopeGreen" x1="0" y1="0" x2="0" y2="1">
            <stop offset="0" stop-color="#7fbb30"/>
            <stop offset="0.6" stop-color="#00912f"/>
            <stop offset="1" stop-color="#00912f"/>
          </linearGradient>
        </defs>
        <polygon class="slope-rule" points="92,330 612,14 612,330" fill="#ffffff"/>
        <polygon class="slope-field" points="145,330 612,46 612,330" fill="url(#slopeGreen)"/>
      </svg>
      <div class="brand brand--front">
        <span class="brand__square"></span>
        <span class="brand__name">
          <span class="brand__short">DGLLC</span>
          <span class="brand__full">Dunleavy Group LLC</span>
        </span>
      </div>
    </div>
    <div class="website"><span>WWW.WEBSITE.COM</span></div>
  </section>

  <section class="card card--back" aria-label="Card back">
    <div class="brand brand--back">
      <span class="brand__square"></span>
      <span class="brand__name">
        <span class="brand__short">DGLLC</span>
        <span class="brand__full">Dunleavy Group LLC</span>
      </span>
    </div>
    <svg class="divider" width="4" height="289" viewBox="0 0 4 289" aria-hidden="true">
      <defs>
        <linearGradient id="dividerFade" x1="0" y1="0" x2="0" y2="1">
          <stop offset="0" stop-color="#0a7ad6"/>
          <stop offset="1" stop-color="#241a63"/>
        </linearGradient>
      </defs>
      <rect x="0.5" y="0" width="3" height="289" fill="url(#dividerFade)"/>
    </svg>
  </section>
</main>
</body>
</html>
```